Mosquito Repellent Wet Wipes pacakage design

We are a mosquito repellent manufacturer under the brand name "Zest Guard". We have a product currently and are looking to make it more attractive.

Our product is a mosquito repellent wipe that can be applied on skin and clothing for protection against mosquitoes. It is going to be available in sachets. Customer age groups include ages 10-30 as well as Moms who are key decision makers.

We are looking for a friendly package in terms of color and appeal and a redesign of Zest Guard logo. I am attaching our current product pictures and brochure. Hope this gets you started. We are attaching information on the spray bottle.

Visit www.tolvanhealthworks.com for more details.

Package Dimension Folded : 80x60 mm
Package Dimension unfolded: 80 x 120 mm

Thank you
Varun
Updates

Project Deadline Extended Reason: Still not happy with the designs that are submitted. Like to see more designs. Added Thursday, February 18, 2016

Target Market(s)

General population with more focus on age groups 10-30 as well as Moms

Industry/Entity Type

Cosmetics

Requirements
Must have
• Statutory information should be provided on the product including Manufacturing address, ingredient name & bar code. I guess we can do this once the package is finalized

```html
<!DOCTYPE html>
<html lang="en">
<head>
<meta charset="utf-8">
<title>Zest Guard – Wipes Carton Dieline</title>
<link href="https://fonts.googleapis.com/css2?family=Oswald:wght@500&family=Lato:wght@400;700&display=swap" rel="stylesheet">
<style>
  :root {
    --bg: #ffffff;
    --flap: #b3e0de;
    --panel: #e9f6f5;
    --teal: #3aa9a4;
    --orange: #e8922a;
    --ink: #555f63;
    --grey: #a9adaf;
    --label: #f2f2f2;
  }
  html, body { margin: 0; padding: 0; overflow: hidden; }
  body { width: 1016px; height: 1200px; background: var(--bg); display: flex; align-items: center; justify-content: center; }
  .dieline { width: 960px; height: 629px; }
  .flap { fill: var(--flap); }
  .panel { fill: var(--panel); }
  .brand { font-family: "Oswald", sans-serif; font-weight: 500; fill: var(--orange); }
  .tagline { font-family: "Lato", sans-serif; font-weight: 700; fill: var(--orange); }
  .maker { font-family: "Lato", sans-serif; font-weight: 700; fill: var(--ink); }
  .small { font-family: "Lato", sans-serif; font-weight: 400; fill: var(--ink); }
  .small-strong { font-family: "Lato", sans-serif; font-weight: 700; fill: var(--ink); }
  .label-text { font-family: "Lato", sans-serif; font-weight: 400; fill: var(--label); }
  .rule { stroke: var(--ink); stroke-width: .5; fill: none; }
  .info-box { stroke: var(--ink); stroke-width: .9; fill: none; }
  .storage { fill: var(--grey); }
</style>
</head>
<body>
<svg class="dieline" viewBox="0 0 580 380" xmlns="http://www.w3.org/2000/svg">
  <defs>
    <linearGradient id="patternTop" x1="0" y1="0" x2="0" y2="1">
      <stop offset="0" stop-color="#5fbdb8"/>
      <stop offset="1" stop-color="#e9f6f5" stop-opacity="0"/>
    </linearGradient>
    <linearGradient id="patternBottom" x1="0" y1="0" x2="0" y2="1">
      <stop offset="0" stop-color="#e9f6f5" stop-opacity="0"/>
      <stop offset="1" stop-color="#7cc8c3"/>
    </linearGradient>
  </defs>

  <!-- glue flap -->
  <polygon class="flap" points="8,108 25,100 25,277 8,270"/>

  <!-- top flaps -->
  <rect class="flap" x="162" y="32" width="136" height="68"/>
  <rect class="flap" x="300" y="8" width="133" height="20" rx="5"/>
  <rect class="panel" x="298" y="30" width="137" height="70"/>
  <rect class="flap" x="435" y="32" width="135" height="68"/>

  <!-- main panels -->
  <rect class="panel" x="25" y="100" width="137" height="177"/>
  <rect class="panel" x="162" y="100" width="136" height="177"/>
  <rect class="panel" x="298" y="100" width="137" height="177"/>
  <rect class="panel" x="435" y="100" width="135" height="177"/>

  <!-- bottom flaps -->
  <rect class="flap" x="25" y="277" width="137" height="73"/>
  <rect class="flap" x="29" y="350" width="129" height="20" rx="5"/>
  <rect class="flap" x="162" y="277" width="136" height="73"/>
  <rect class="flap" x="298" y="277" width="137" height="73"/>
  <rect class="flap" x="435" y="277" width="135" height="73"/>

  <!-- front panel -->
  <g class="front">
    <rect x="25" y="100" width="137" height="35" fill="url(#patternTop)" role="img" aria-label="Teal triangle mosaic pattern"/>
    <text class="brand" x="93" y="195" font-size="21" text-anchor="middle">Zest Guard</text>
    <text class="tagline" x="93" y="207" font-size="4.5" text-anchor="middle">Anti Mosquito Body Sponge</text>
    <rect x="25" y="222" width="137" height="55" fill="url(#patternBottom)" role="img" aria-label="Teal triangle mosaic pattern"/>
    <text class="maker" x="93" y="261" font-size="8" text-anchor="middle">Tolvan Health</text>
  </g>

  <!-- side panel: ingredients -->
  <g class="side-info">
    <text class="brand" x="230" y="122" font-size="10" text-anchor="middle">Zest Guard</text>
    <text class="small" x="230" y="146" font-size="4" text-anchor="middle" font-style="italic">Ingredients:</text>
    <text class="small" x="230" y="153" font-size="4" text-anchor="middle" font-style="italic">100% Pure XXXXXXXXXXXXX</text>
    <rect class="info-box" x="194" y="158" width="72" height="62" rx="4"/>
    <text class="small" x="230" y="166" font-size="3.5" text-anchor="middle">Information</text>
    <line class="rule" x1="200" y1="182" x2="260" y2="182"/>
    <line class="rule" x1="200" y1="196" x2="260" y2="196"/>
    <text class="small" x="230" y="231" font-size="4" text-anchor="middle">Xxxxxxxxx xxxxxx xxxxxxx xxxxxxx</text>
    <rect class="storage" x="204" y="250" width="52" height="15"/>
    <text class="label-text" x="207" y="256" font-size="3">Store in a cool</text>
    <text class="label-text" x="207" y="261" font-size="3">dry place</text>
  </g>

  <!-- second front panel -->
  <g class="front-alt">
    <rect x="298" y="30" width="137" height="105" fill="url(#patternTop)" role="img" aria-label="Teal triangle mosaic pattern"/>
    <text class="brand" x="405" y="58" font-size="9" text-anchor="middle">Zest Guard</text>
    <text class="brand" x="366" y="195" font-size="21" text-anchor="middle">Zest Guard</text>
    <text class="tagline" x="366" y="207" font-size="4.5" text-anchor="middle">Anti Mosquito Body Sponge</text>
    <rect x="298" y="222" width="137" height="55" fill="url(#patternBottom)" role="img" aria-label="Teal triangle mosaic pattern"/>
    <text class="maker" x="366" y="261" font-size="8" text-anchor="middle">Tolvan Health</text>
  </g>

  <!-- side panel: maker details -->
  <g class="side-maker">
    <text class="brand" x="502" y="122" font-size="10" text-anchor="middle">Zest Guard</text>
    <circle cx="492" cy="160" r="5" fill="#fff" stroke="#c0392b" stroke-width="1"/>
    <line x1="488.5" y1="156.5" x2="495.5" y2="163.5" stroke="#c0392b" stroke-width="1"/>
    <path d="M508,156 l3,5 h-6 z M505,164 h6" fill="none" stroke="var(--ink)" stroke-width=".9"/>
    <text class="small" x="502" y="180" font-size="3.2" text-anchor="middle" font-style="italic">Produced &amp; packed by:</text>
    <text class="small-strong" x="502" y="186" font-size="3.2" text-anchor="middle">Zest Guard</text>
    <text class="small" x="502" y="191" font-size="3.2" text-anchor="middle">12 Harbor Lane, Westfield</text>
    <text class="small" x="502" y="200" font-size="3.2" text-anchor="middle">hello@zestguard.com</text>
    <text class="small" x="502" y="205" font-size="3.2" text-anchor="middle">www.zestguard.com</text>
  </g>
</svg>
</body>
</html>
```